LA's Newest HEMP Facial Oil and Body Oil Packaging Project

We need a packaging concept for a Hemp based facial oil and body oil. We need label design for the bottle and carton graphics. I am attaching a few reference photos. The target demographic is women between 17-35 year old. Products need to be able to stand out in crowded stores with clear calls to action.
1oz Dropper Bottle with Unit Carton - Hemp Facial Oil
4oz PET Bottle with Unit Carton - Hemp + Rose Facial Oil

```html
<!DOCTYPE html>
<html lang="en">
<head>
<meta charset="utf-8">
<title>Hemp+Rose Facial Oil – Bottle Label</title>
<link rel="stylesheet" href="https://fonts.googleapis.com/css2?family=Lato:wght@400;700&family=Montserrat:wght@400;800;900&family=Pinyon+Script&display=swap">
<style>
  :root {
    --backdrop: #9a9b9f;
    --label-light: #f8f8f8;
    --label-mid: #e4e5e7;
    --panel-white: #ffffff;
    --accent-red: #ee3a43;
    --text-grey: #505050;
    --facts-dark: #3e3f41;
    --barcode-grey: #545456;
    --rose-pink: #f6a9b1;
    --rose-deep: #ef4650;
  }
  * { margin: 0; padding: 0; box-sizing: border-box; }
  html, body { width: 1200px; height: 720px; overflow: hidden; }
  body {
    background: var(--backdrop);
    font-family: "Lato", Arial, sans-serif;
    position: relative;
  }
  .label {
    position: absolute; left: 0; top: 60px;
    width: 1200px; height: 600px; overflow: hidden;
    background:
      radial-gradient(circle at 240px 260px, rgba(255,255,255,.9) 0, rgba(255,255,255,0) 260px),
      radial-gradient(circle at 1000px 500px, rgba(255,250,240,.9) 0, rgba(255,255,255,0) 240px),
      radial-gradient(circle at 60px 560px, rgba(255,255,255,.6) 0, rgba(255,255,255,0) 200px),
      linear-gradient(135deg, var(--label-light) 0%, var(--label-mid) 100%);
  }
  .abs { position: absolute; }
  .heading-red { color: var(--accent-red); font-weight: 700; font-size: 22px; line-height: 26px; letter-spacing: -.2px; }
  .body-copy { color: var(--text-grey); font-weight: 700; font-size: 20px; line-height: 24px; letter-spacing: -.2px; }

  .center-panel { left: 426px; top: 0; width: 348px; height: 600px; background: var(--panel-white); }
  .product-title {
    left: 426px; top: 60px; width: 348px; text-align: center;
    font-family: "Montserrat", Arial, sans-serif; font-weight: 900;
    font-size: 53px; line-height: 56px; color: var(--accent-red); letter-spacing: -.5px;
  }
  .skin-tagline {
    left: 468px; top: 216px; width: 264px; height: 24px;
    border: 1.5px solid var(--accent-red);
  }
  .skin-tagline span {
    position: absolute; left: 0; right: 0; top: -22px; text-align: center;
    font-family: "Pinyon Script", cursive; font-size: 38px; color: #555; white-space: nowrap;
  }
  .with-line { right: 468px; top: 286px; text-align: right; font-size: 23px; line-height: 24px; }
  .rose-art {
    left: 378px; top: 280px; width: 420px; height: 280px;
  }
  .size-badge {
    left: 538px; top: 538px; width: 126px; height: 126px; border-radius: 50%;
    background: var(--accent-red); color: #fff; text-align: center;
    font-size: 28px; font-weight: 700; padding-top: 18px;
  }

  .barcode-box {
    left: 28px; top: 462px; width: 188px; height: 104px; background: var(--barcode-grey);
    color: #fff; font-size: 20px; display: flex; align-items: center; justify-content: center;
  }

  .facts-box {
    left: 820px; top: 47px; width: 360px; height: 223px;
    border: 3px solid var(--facts-dark); background: #fff;
    font-family: "Montserrat", Arial, sans-serif; color: var(--facts-dark);
    padding: 4px 9px 0 10px;
  }
  .facts-title { font-weight: 800; font-size: 27px; line-height: 34px; }
  .facts-serving { font-size: 14px; line-height: 19px; margin-top: 6px; }
  .facts-rule-thick { height: 7px; background: var(--facts-dark); margin-top: 11px; }
  .facts-row { display: flex; justify-content: space-between; font-size: 13px; line-height: 19.5px; }
  .facts-rows { margin-top: 4px; }
  .facts-rule-thin { height: 1.5px; background: var(--facts-dark); margin-top: 6px; }
  .facts-note { font-size: 13px; line-height: 19.5px; margin-top: 3px; }
</style>
</head>
<body>
<main class="label">
  <section class="abs" style="left:28px;top:46px;width:380px;">
    <h2 class="heading-red">SHAKE WELL BEFORE USE</h2>
    <p class="body-copy">Lorem ipsum dolor sit amet, consectetuer adipiscing elit, sed diam nonummy nibh euismod tincidunt ut.</p>
    <p class="body-copy" style="margin-top:25px;">Lorem ipsum dolor sit amet, consectetuer adipiscing elit, sed diam nonummy nibh euismod tincidunt ut laoreet dolore magna aliquam erat volutpat. Ut wisi enim ad minim</p>
    <h2 class="heading-red" style="margin-top:32px;">Manufacture by:</h2>
    <p class="body-copy">Lorem ipsum dolor sit amet, consectetuer adipiscing elit, sed diam nonummy nibh euismod tincidunt ut.</p>
  </section>

  <div class="abs barcode-box">bar code</div>
  <p class="abs heading-red" style="left:231px;top:462px;">Expiry date:</p>
  <p class="abs heading-red" style="left:231px;top:509px;">Issue Date:</p>

  <div class="abs center-panel"></div>
  <h1 class="abs product-title">Hemp+Rose<br>Facial Oil</h1>
  <div class="abs skin-tagline"><span>For all skin types</span></div>

  <svg class="abs rose-art" viewBox="0 0 420 280" role="img" aria-label="Illustration of a pink rose with fine lilac flower sprigs">
    <defs>
      <radialGradient id="roseGlow" cx="50%" cy="50%" r="50%">
        <stop offset="0" stop-color="var(--rose-deep)"/>
        <stop offset=".45" stop-color="var(--rose-pink)"/>
        <stop offset="1" stop-color="#fbd3d7"/>
      </radialGradient>
      <linearGradient id="sprigTone" x1="0" x2="1">
        <stop offset="0" stop-color="#d7d4ef" stop-opacity=".9"/>
        <stop offset="1" stop-color="#e7e5f5" stop-opacity="0"/>
      </linearGradient>
    </defs>
    <ellipse cx="300" cy="130" rx="120" ry="90" fill="url(#sprigTone)"/>
    <ellipse cx="133" cy="142" rx="133" ry="138" fill="url(#roseGlow)"/>
  </svg>

  <p class="abs heading-red with-line">WITH<br>HEMP OIL<br>&amp; ROSE</p>
  <div class="abs size-badge">4oz</div>

  <section class="abs facts-box">
    <h2 class="facts-title">Supplemental Facts:</h2>
    <p class="facts-serving">Serving Size: 1 mL dropper (approx 0.5ml)<br>Servings per container:&nbsp; 15</p>
    <div class="facts-rule-thick"></div>
    <div class="facts-rows">
      <div class="facts-row"><span>Amount Per Serving</span><span>% Daily Value</span></div>
      <div class="facts-row"><span style="font-weight:400;">Hemp Derived Cannabidiol</span><span>16.67 mg</span></div>
      <div class="facts-row"><span>Cannabidiol (CBD) 250 mg</span><span>*</span></div>
    </div>
    <div class="facts-rule-thin"></div>
    <p class="facts-note">*Daily Value not established<br>Cannabidiol is a natural constituent of Hemp Oil</p>
  </section>

  <section class="abs" style="left:828px;top:284px;width:360px;">
    <h2 class="heading-red">Other Ingredients:</h2>
    <p class="body-copy" style="font-weight:400;margin-top:9px;">Hemp Seed oil, Rose</p>
    <h2 class="heading-red" style="margin-top:8px;">WARNING:</h2>
    <p class="body-copy" style="margin-top:5px;">Lorem ipsum dolor sit amet, consectetuer adipiscing elit, sed diam nonummy nibh euismod tincidunt ut laoreet dolore magna.</p>
  </section>
</main>
</body>
</html>
```